Design of business signage for outside store front

We need signage designed for outside a store front.  We already have a logo, colours and font that we would like to use but would like some ideas as regards layout/design of the signage.  The final product will be for the use of the installer to produce and install the signage.  Attached are files with our logo and font and a picture of the current signage which needs to be replaced.  The size and shape of the signage will be the same as the current signage, its just the design/layout that we would like changed.
N.B. We would like two versions if possible, one with the web address and one without the web address to see what they look like.

```html
<!DOCTYPE html>
<html lang="en">
<head>
<meta charset="utf-8">
<title>Gusto Ibérico – Storefront Sign</title>
<link rel="stylesheet" href="https://fonts.googleapis.com/css2?family=Marcellus&family=Montserrat:wght@400;500&display=swap">
<style>
  :root {
    --backdrop: #808080;
    --maroon: #8E3A43;
    --sun: #F4D443;
    --paper: #FFFFFF;
    --ink: #3A3A3A;
  }
  html, body {
    margin: 0;
    padding: 0;
    width: 1200px;
    height: 715px;
    overflow: hidden;
    background: var(--backdrop);
  }
  .sign {
    position: absolute;
    left: 40px;
    top: 96px;
    width: 1120px;
    height: 522px;
    background: var(--paper);
    overflow: hidden;
  }
  .sign__bands {
    position: absolute;
    inset: 0;
  }
  .band--maroon { fill: var(--maroon); }
  .band--sun { fill: var(--sun); }
  .url-bar { fill: var(--maroon); }

  .brand {
    position: absolute;
    left: 433px;
    top: 60px;
    width: 253px;
    display: flex;
    flex-direction: column;
    align-items: center;
  }
  .brand__square {
    width: 173px;
    height: 173px;
    background: var(--maroon);
  }
  .brand__name {
    margin-top: 18px;
    font-family: "Marcellus", serif;
    font-size: 25px;
    letter-spacing: 1px;
    color: var(--maroon);
    white-space: nowrap;
    line-height: 1;
  }
  .brand__tagline {
    margin-top: 14px;
    font-family: "Montserrat", sans-serif;
    font-weight: 400;
    font-size: 9px;
    letter-spacing: 3.4px;
    color: var(--ink);
    white-space: nowrap;
  }
  .web-address {
    position: absolute;
    left: 369px;
    top: 443px;
    width: 494px;
    height: 53px;
    display: flex;
    align-items: center;
    justify-content: center;
    font-family: "Montserrat", sans-serif;
    font-weight: 500;
    font-size: 29px;
    color: var(--paper);
    letter-spacing: 0.3px;
  }
</style>
</head>
<body>
  <div class="sign">
    <svg class="sign__bands" width="1120" height="522" viewBox="0 0 1120 522" aria-hidden="true">
      <polygon class="band--maroon" points="0,0 218,0 357,522 0,522"/>
      <polygon class="band--sun" points="762,0 1120,0 1120,522 901,522"/>
      <polygon class="url-bar" points="362,443 856,443 870,496 376,496"/>
    </svg>

    <div class="brand">
      <div class="brand__square"></div>
      <div class="brand__name">GUSTO IBÉRICO</div>
      <div class="brand__tagline">Spanish Artisan Foods</div>
    </div>

    <div class="web-address">www.gustoiberico.com.au</div>
  </div>
</body>
</html>
```